Magical healing ointment looking for new branded labels

I need a new product label for my healing comfrey ointments, which started as just a simple ointment, and has grown to include a few varients including a body oil and lip balm. It sells quite well when I have a market, which I don't always have time to do - so I'd like to take it and leave it with some health shops, however for this I'd really like a more professional label to take these products further.

The company name is Brightwren Meadow - slogan Natural by Nature; as I am both a healer that makes ointments and yet also make scarves, cowls with high quality natural wool.
The ointment is simply called 'Comfrey Ointment', don't mind if it has Magical or healing in front of it. It's made by me, with high quality all natural, locally sourced organic ingredients, and supports the healing of bones, injuries, RSI, arthritis, rheuma, eczema, aches and pains.. Comfrey itself is an ancient herb also used in medieval herblore and by the ancient romans, so my keys words are to get feeling for the brand:
Timeless/ classic/ clean/ natural/ quality/ confident/ healing

I would like the labels to stand out, and look professional. The smallest size is 6 x 2.5 cm, this is an amber small jar of 30ml, the larger jar is double that size at 60ml, and the bottles bigger. I would like to be able to add a bit on the side if needed to add ingredients, and be able to scale the label up or down depending on the size of the jar. On top of this would like to be able to text as needed depending on the product in the jar.

Have included my company logo - for an idea of what that looks like, please note though that this branding or style doesn't need to include this logo, nor look like this logo. I've also included an example of someone who I think is doing a good job of being unique, simple, classic and appealing. Let me know if you have any questions. Thanks!

Target Market(s)

People with an eco-sustainable mind-set that are looking to resolve ailments naturally.

Industry/Entity Type

Health

Requirements
Must have
• The product name, and company name
Nice to have
• I'd like to leave most of the design to the designers ideas, however am ok to have leaves - or natural elements that support the typography, but not overwhelm it.

```html
<!DOCTYPE html>
<html lang="en">
<head>
<meta charset="utf-8">
<title>Comfrey Ointment Label</title>
<link rel="stylesheet" href="https://fonts.googleapis.com/css2?family=Yesteryear&family=IM+Fell+English+SC&family=Federo&display=swap">
<style>
  :root {
    --ink: #111111;
    --herb-green: #2e5b2c;
    --paper: #ffffff;
    --ornament-tone: #3a3a3a;
  }
  * { margin: 0; padding: 0; box-sizing: border-box; }
  html, body {
    width: 1200px;
    height: 900px;
    overflow: hidden;
    background: var(--paper);
  }
  .label {
    position: relative;
    width: 1200px;
    height: 900px;
    background: var(--paper);
  }
  .label-frame {
    position: absolute;
    inset: 0;
  }
  .label-text {
    position: absolute;
    left: 0;
    width: 1200px;
    text-align: center;
    white-space: nowrap;
    line-height: 1;
    font-weight: 400;
  }
  .claim-script {
    font-family: "Yesteryear", cursive;
    color: var(--herb-green);
  }
  .claim-top {
    top: 132px;
    font-size: 88px;
    letter-spacing: 3px;
  }
  .claim-bottom {
    top: 684px;
    font-size: 80px;
    letter-spacing: 2px;
  }
  .product-name {
    font-family: "IM Fell English SC", serif;
    color: var(--herb-green);
    font-size: 140px;
    letter-spacing: 1px;
  }
  .product-line-one { top: 266px; }
  .product-line-two { top: 416px; }
  .maker-name {
    top: 600px;
    font-family: "Federo", sans-serif;
    color: var(--ink);
    font-size: 44px;
    letter-spacing: 1px;
  }
</style>
</head>
<body>
<main class="label">
  <svg class="label-frame" width="1200" height="900" viewBox="0 0 1200 900" xmlns="http://www.w3.org/2000/svg">
    <g class="rule-lines" stroke="var(--ink)" stroke-width="4">
      <line x1="275" y1="85" x2="455" y2="85"/>
      <line x1="785" y1="85" x2="962" y2="85"/>
      <line x1="275" y1="825" x2="455" y2="825"/>
      <line x1="785" y1="825" x2="962" y2="825"/>
    </g>
    <rect class="ornament ornament-top" x="482" y="22" width="272" height="52" rx="26" fill="var(--ornament-tone)" role="img" aria-label="Symmetrical calligraphic flourish ornament"/>
    <rect class="ornament ornament-bottom" x="482" y="808" width="272" height="62" rx="28" fill="var(--ornament-tone)" role="img" aria-label="Symmetrical calligraphic flourish ornament"/>
    <polygon class="ribbon ribbon-top" points="229,121 1011,121 987,179 1011,234 229,234 253,179" fill="var(--paper)" stroke="var(--ink)" stroke-width="9" stroke-linejoin="miter"/>
    <polygon class="ribbon ribbon-bottom" points="229,676 1011,676 987,733 1011,788 229,788 253,733" fill="var(--paper)" stroke="var(--ink)" stroke-width="9" stroke-linejoin="miter"/>
    <g class="maker-band" fill="var(--ink)">
      <polygon points="218,612 360,612 360,643 218,643 242,627"/>
      <polygon points="872,612 1020,612 996,627 1020,643 872,643"/>
    </g>
  </svg>

  <p class="label-text claim-script claim-top">All- Natural</p>
  <h1 class="label-text product-name product-line-one">Comfrey</h1>
  <h1 class="label-text product-name product-line-two">Ointment</h1>
  <p class="label-text maker-name">Brightwren Meadow</p>
  <p class="label-text claim-script claim-bottom">Organic</p>
</main>
</body>
</html>
```